Tumble Tail (Pet Supplies) Home Page

For our Tumble Tail website, we want this to be fun and playful but with a touch of your creativity! Tumble Tail is a fun-loving brand that sells pet supplies and accessories focused on accentuating the love between pets and their owners. We want to advertise these products in a welcoming way, making the customer receive the happiness the brand offers.

Target Market(s)

Main demo: Female pet owners online shopping 18-34. Secondary demo: All pet owners online shopping 18-34.

Number of Pages Required

1 page

```html
<!DOCTYPE html>
<html lang="en">
<head>
<meta charset="utf-8">
<title>Tumble Tail – Pet Supplies</title>
<link href="https://fonts.googleapis.com/css2?family=Bubblegum+Sans&family=Delius&display=swap" rel="stylesheet">
<style>
:root{
  --teal:#4fbcc4;
  --teal-dark:#3aa9b2;
  --teal-soft:#8fd4d9;
  --ink:#2b2b2b;
  --body:#444;
  --white:#fff;
  --grey:#9a9a9a;
  --purple:#5b5fc7;
}
*{margin:0;padding:0;box-sizing:border-box}
html,body{width:1200px;height:3498px;overflow:hidden;background:var(--white)}
body{position:relative;font-family:"Delius",cursive;color:var(--body)}
.abs{position:absolute}
.display{font-family:"Bubblegum Sans",cursive}

/* header */
.top-rule{left:0;top:0;width:1200px;height:8px;background:var(--teal)}
.brand{left:54px;top:30px;display:flex;align-items:center;gap:10px;color:var(--teal);font-family:"Bubblegum Sans",cursive;font-size:30px}
.brand .dot{width:22px;height:22px;border-radius:50%;background:var(--teal)}
.nav{left:387px;top:44px;display:flex;font-family:"Bubblegum Sans",cursive;font-size:20px;color:var(--ink)}
.nav span{position:absolute;white-space:nowrap}
.nav .active{color:var(--teal)}
.social{display:flex;gap:12px}
.social i{display:block;width:22px;height:22px;border-radius:5px;background:var(--teal)}
.social.head{left:1014px;top:46px}

/* hero */
.hero-photo{left:0;top:106px;width:1200px;height:661px;background:linear-gradient(180deg,#8f9d53 0%,#5d7a2f 35%,#3f6d22 70%,#2f5a1b 100%)}
.hero-wave{left:0;top:640px;width:1200px;height:130px}
.hero-welcome{left:695px;top:326px;font-family:"Bubblegum Sans",cursive;font-size:40px;color:var(--teal)}
.hero-title{left:695px;top:366px;font-family:"Bubblegum Sans",cursive;font-size:82px;color:var(--white);line-height:1}
.btn-solid{left:695px;top:476px;width:171px;height:42px;border-radius:21px;background:var(--teal);color:var(--white);font-family:"Bubblegum Sans",cursive;font-size:19px;display:flex;align-items:center;justify-content:center;box-shadow:8px 0 0 var(--white)}
.dots{left:858px;top:649px;display:flex;gap:6px}
.dots i{display:block;width:18px;height:8px;border-radius:4px;background:var(--white)}
.dots i:first-child{background:var(--teal)}

/* section headings */
.h2{font-family:"Bubblegum Sans",cursive;font-size:50px;color:var(--teal);line-height:1}
.copy{font-size:15px;line-height:24.5px;color:var(--body)}

/* story */
.story-h{left:54px;top:830px}
.story-p1{left:54px;top:898px;width:480px}
.story-p2{left:54px;top:1044px;width:480px}
.btn-outline{left:54px;top:1137px;width:171px;height:44px;border:2px solid var(--teal);border-radius:22px;color:var(--teal);font-family:"Bubblegum Sans",cursive;font-size:19px;display:flex;align-items:center;justify-content:center;box-shadow:6px 0 0 var(--teal)}
.story-photo{left:652px;top:835px;width:495px;height:373px;border-radius:40px;background:radial-gradient(ellipse at 50% 55%,#c9a27a 0%,#e2cfb8 45%,#ffffff 75%)}

/* shop */
.shop{left:0;top:1266px;width:1200px;height:494px;background:var(--teal)}
.shop-h{left:38px;top:1292px;color:var(--white);font-size:50px}
.card{top:1371px;width:217px;height:241px;background:var(--white);border-radius:38px 0 56px 0}
.card.framed{box-shadow:5px -5px 0 #a8a8a8}
.card .thumb{position:absolute;left:50%;top:50px;transform:translateX(-50%);border-radius:10px}
.card .stars{position:absolute;left:14px;bottom:10px;color:var(--teal);font-size:19px;letter-spacing:1px}
.badge{left:360px;top:1371px;width:88px;height:34px;background:#9b9b9b;color:var(--white);font-family:"Bubblegum Sans",cursive;font-size:19px;display:flex;align-items:center;justify-content:center}
.prod{top:1620px;width:217px;color:var(--white)}
.prod .name{font-family:"Bubblegum Sans",cursive;font-size:22px;line-height:1.2}
.prod .desc{font-size:12px;line-height:20px;white-space:nowrap;margin-top:4px}
.prod .price{font-family:"Bubblegum Sans",cursive;font-size:24px;margin-top:6px}

/* we love pets */
.love-photo{left:75px;top:1825px;width:447px;height:346px;border-radius:50%;background:radial-gradient(ellipse at 40% 45%,#efe6da 0%,#f6f1ea 45%,#ffffff 72%)}
.love-h{left:581px;top:1856px}
.love-p{left:582px;top:1918px;width:570px}

/* testimonials */
.testi-h{left:0;top:2222px;width:1200px;text-align:center}
.testi-card{left:160px;top:2280px;width:878px;height:434px}
.testi-name{left:627px;top:2430px;font-family:"Bubblegum Sans",cursive;font-size:34px;color:var(--white)}
.testi-quote{left:627px;top:2485px;width:400px;font-size:14px;line-height:25px;color:var(--white)}
.arrow{width:26px;height:40px}

/* promo */
.rabbit{left:41px;top:2795px;width:163px;height:150px;border-radius:50% 50% 0 0;background:radial-gradient(ellipse at 50% 65%,#8a6a4a 0%,#b89a78 45%,#ffffff 75%)}
.pair{left:740px;top:2768px;width:360px;height:217px;border-radius:50% 50% 0 0;background:radial-gradient(ellipse at 45% 60%,#b25a22 0%,#c98552 40%,#ffffff 75%)}
.promo-band{left:0;top:2920px;width:1200px;height:310px}
.promo-sale{left:43px;top:2990px;color:var(--white);font-family:"Bubblegum Sans",cursive;font-size:60px;line-height:1}
.promo-sale small{font-size:32px}
.promo-love{right:56px;top:3162px;color:var(--white);font-family:"Bubblegum Sans",cursive;font-size:40px;line-height:1}
.rewards{left:0;top:3198px;width:152px;height:62px;border-radius:31px;background:var(--purple);color:var(--white);font-size:17px;display:flex;align-items:center;justify-content:center;gap:8px}
.rewards i{display:block;width:20px;height:18px;border-radius:3px;background:var(--white)}
.chat{left:1136px;top:3198px;width:64px;height:64px;border-radius:50%;background:#dff1f5;display:flex;align-items:center;justify-content:center}

/* footer */
.foot-brand{left:54px;top:3334px;display:flex;align-items:center;gap:10px;color:var(--teal);font-family:"Bubblegum Sans",cursive;font-size:40px}
.foot-brand .dot{width:28px;height:28px;border-radius:50%;background:var(--teal)}
.foot-about{left:258px;top:3292px;width:260px;font-size:14px;line-height:22.5px}
.foot-col{top:3272px}
.foot-col h4{font-family:"Bubblegum Sans",cursive;font-weight:400;font-size:22px;color:var(--teal);margin-bottom:10px}
.foot-col li{list-style:none;font-size:14px;line-height:31px;color:var(--body);white-space:nowrap}
.foot-col li::before{content:"» ";color:var(--body)}
.social.foot{left:977px;top:3401px}
.foot-rule{left:38px;top:3451px;width:1124px;height:1px;background:var(--teal)}
.copyright{left:0;top:3463px;width:1200px;text-align:center;font-family:"Bubblegum Sans",cursive;font-size:19px;color:var(--teal)}
</style>
</head>
<body>

<!-- header -->
<div class="abs top-rule"></div>
<div class="abs brand"><span class="dot"></span>Tumble Tail</div>
<nav class="abs nav">
  <span class="active" style="left:0">Home</span>
  <span style="left:83px">Shop Our</span>
  <span style="left:195px">Story</span>
  <span style="left:282px">Blog</span>
  <span style="left:354px">Pet History</span>
  <span style="left:484px">Contact Us</span>
</nav>
<div class="abs social head"><i></i><i></i><i></i><i></i></div>

<!-- hero -->
<div class="abs hero-photo" role="img" aria-label="Photo of a laughing boy playing with a ball and a jumping terrier on a green lawn"></div>
<svg class="abs hero-wave" viewBox="0 0 1200 130" preserveAspectRatio="none">
  <path d="M0,127 C180,70 360,48 520,52 C760,58 980,110 1200,122 L1200,130 L0,130 Z" fill="#fff"/>
  <path d="M0,127 C180,70 360,48 520,52 C760,58 980,110 1200,122" fill="none" stroke="#4fbcc4" stroke-width="5"/>
</svg>
<div class="abs hero-welcome">Welcome To</div>
<div class="abs hero-title">Tumble Tail</div>
<div class="abs btn-solid">Contact Us</div>
<div class="abs dots"><i></i><i></i><i></i></div>

<!-- our story -->
<h2 class="abs h2 story-h">Our Story</h2>
<p class="abs copy story-p1">It is a long established fact that a reader will be distracted by the readable content of a page when looking at its layout. The point of using Lorem Ipsum is that it has a more-or-less normal distribution of letters, as opposed to using 'Content here, content here', making it look like readable English.</p>
<p class="abs copy story-p2" style="top:1044px">Lorem Ipsum is that it has a more-or-less normal distribution of letters, as opposed to using 'Content here, content here', making it look like readable English.</p>
<div class="abs btn-outline">Read More &raquo;</div>
<div class="abs story-photo" role="img" aria-label="Photo of four small dogs wearing colourful bow ties"></div>

<!-- shop -->
<section class="abs shop"></section>
<h2 class="abs h2 shop-h">Shop Our</h2>

<div class="abs card" style="left:-30px"><div class="thumb" style="width:170px;height:40px;top:90px;background:linear-gradient(90deg,#f08a3c,#4aa6d8,#f08a3c)" role="img" aria-label="Braided dog leash"></div><div class="stars">★★★★★</div></div>
<div class="abs card" style="left:232px"><div class="thumb" style="width:100px;height:140px;top:40px;background:linear-gradient(180deg,#e9eef5,#3a7cc8)" role="img" aria-label="Bag of soft baked dog treats"></div><div class="stars">★★★★</div></div>
<div class="abs badge">10% OFF</div>
<div class="abs card framed" style="left:491px"><div class="thumb" style="width:120px;height:130px;top:50px;background:linear-gradient(180deg,#dfe8ec,#7fd0e6)" role="img" aria-label="Wire pet crate with blue tray"></div><div class="stars">★★★★★</div></div>
<div class="abs card" style="left:752px"><div class="thumb" style="width:80px;height:150px;top:40px;background:linear-gradient(180deg,#e8e8ea,#9a9aa2)" role="img" aria-label="Bag of cat food"></div><div class="stars">★★★★</div></div>
<div class="abs card" style="left:1012px"><div class="thumb" style="width:170px;height:40px;top:90px;background:linear-gradient(90deg,#f08a3c,#4aa6d8,#f08a3c)" role="img" aria-label="Braided dog leash"></div><div class="stars">★★★★★</div></div>

<div class="abs prod" style="left:-30px"><div class="name">Product Name</div><div class="desc">Lorem Ipsum is simply dummy text<br>of the printing industry Ipsum</div><div class="price">$ 127</div></div>
<div class="abs prod" style="left:232px"><div class="name">Product Name</div><div class="desc">Lorem Ipsum is simply dummy text<br>of the printing industry Ipsum</div><div class="price">$ 132</div></div>
<div class="abs prod" style="left:491px"><div class="name">Product Name</div><div class="desc">Lorem Ipsum is simply dummy text<br>of the printing industry Ipsum</div><div class="price">$ 234</div></div>
<div class="abs prod" style="left:752px"><div class="name">Product Name</div><div class="desc">Lorem Ipsum is simply dummy text<br>of the printing industry Ipsum</div><div class="price">$ 226</div></div>
<div class="abs prod" style="left:1012px"><div class="name">Product Name</div><div class="desc">Lorem Ipsum is simply dummy text<br>of the printing industry Ipsum</div><div class="price">$ 100</div></div>

<!-- we love pets -->
<div class="abs love-photo" role="img" aria-label="Photo of a white puppy beside a colourful knotted ball toy"></div>
<h2 class="abs h2 love-h">We Love Pets</h2>
<div class="abs love-p">
  <p class="copy">It is a long established fact that a reader will be distracted by the readable content of a page when looking at its layout. The point of using Lorem Ipsum is that it has a more-or-less normal distribution of letters, as opposed to using 'Content here, content here', making it look like readable English.</p>
  <p class="copy" style="margin-top:24px">Lorem Ipsum is that it has a more-or-less normal distribution of letters, as opposed to using 'Content here, content here', making it look like readable English. It is a long established fact that a reader will be distracted by the readable content of a page when looking at its layout. The point of using Lorem Ipsum.</p>
</div>

<!-- testimonials -->
<h2 class="abs h2 testi-h">Testimonials</h2>
<svg class="abs testi-card" viewBox="0 0 878 434">
  <defs>
    <clipPath id="card-shape">
      <path d="M22,0 C300,8 600,48 820,12 Q872,4 878,52 L878,396 Q878,440 830,432 C600,402 300,382 42,426 Q0,432 0,392 L0,28 Q0,0 22,0 Z"/>
    </clipPath>
    <linearGradient id="grass" x1="0" y1="0" x2="0" y2="1">
      <stop offset="0" stop-color="#6f9a3c"/>
      <stop offset="1" stop-color="#3f6f22"/>
    </linearGradient>
  </defs>
  <g clip-path="url(#card-shape)">
    <rect width="878" height="434" fill="#4fbcc4"/>
    <rect width="440" height="434" fill="url(#grass)" role="img" aria-label="Photo of a fluffy cream Pomeranian sitting on grass"/>
  </g>
</svg>
<div class="abs testi-name">Bella (dog) “</div>
<p class="abs testi-quote">Before Tumble Tail my human bought me gifts that made me want to dig a hole under the fence and run. Now I still dig, but it's to bury all my awesome toys!”</p>
<svg class="abs arrow" style="left:110px;top:2477px" viewBox="0 0 26 40"><path d="M20,6 L6,20 L20,34" fill="none" stroke="#4fbcc4" stroke-width="5" stroke-linecap="round" stroke-linejoin="round"/></svg>
<svg class="abs arrow" style="left:1064px;top:2477px" viewBox="0 0 26 40"><path d="M6,6 L20,20 L6,34" fill="none" stroke="#4fbcc4" stroke-width="5" stroke-linecap="round" stroke-linejoin="round"/></svg>

<!-- promo -->
<div class="abs rabbit" role="img" aria-label="Photo of a brown rabbit"></div>
<div class="abs pair" role="img" aria-label="Photo of a golden dog and a calico cat nuzzling"></div>
<svg class="abs promo-band" viewBox="0 0 1200 310" preserveAspectRatio="none">
  <path d="M0,12 C250,10 500,70 760,64 C950,60 1100,20 1200,2 L1200,310 L0,310 Z" fill="#4fbcc4"/>
</svg>
<div class="abs promo-sale">“50% OFF <small>sale going on now!</small></div>
<div class="abs promo-love">Because we love you too”.</div>
<div class="abs rewards"><i></i>Rewards</div>
<div class="abs chat"><svg width="28" height="22" viewBox="0 0 28 22"><rect x="1" y="1" width="26" height="16" rx="6" fill="#4fbcc4"/><path d="M6,16 L4,21 L11,16 Z" fill="#4fbcc4"/><rect x="7" y="8" width="14" height="2" rx="1" fill="#fff"/></svg></div>

<!-- footer -->
<div class="abs foot-brand"><span class="dot"></span>Tumble Tail</div>
<p class="abs foot-about">It is a long established fact that a reader will be distracted by the readable content of a page when looking at its layout. The point of using Lorem Ipsum</p>
<div class="abs foot-col" style="left:574px">
  <h4>COMPANY</h4>
  <ul><li>Shop</li><li>Our Story</li><li>Boop Blog</li><li>Pet History 1010</li></ul>
</div>
<div class="abs foot-col" style="left:772px">
  <h4>HELP &amp; SUPPORT</h4>
  <ul><li>Returns &amp; Exchanges</li><li>FAQ</li><li>help@tumbletail.com</li><li>Search</li></ul>
</div>
<div class="abs foot-col" style="left:1004px">
  <h4>CONTACT:</h4>
  <ul><li>555-0142-318</li><li>help@tumbletail.com</li></ul>
</div>
<div class="abs social foot"><i></i><i></i><i></i><i></i><i></i></div>
<div class="abs foot-rule"></div>
<div class="abs copyright">Copyright © 2021 tumbletail.com: All rights reserved</div>

</body>
</html>
```